Business Card Design Project

I am opening a skin care studio called Glow Haven by Marisol. I will be offering a wide range of unique and affordable skin services including facials, chemical peels, microdermabrasion treatments, body wraps, salt glows, all waxing and eye lash extensions. If the business cards depicts what I would like, this would lead to brochures, web design, signs, etc.
Updates

Project Deadline Extended
Reason: A request to extend deadline was requested. I will be more than happy to accommodate.

Industry/Entity Type

Business

Requirements
Nice to have
• facial features so prospective client clearly identifies what type of business this is. Not stuffy or boring "spa" looking graphics. I am focusing just on face, body, waxing, eyelashes. No massage or nails.

```html
<!DOCTYPE html>
<html lang="en">
<head>
<meta charset="utf-8">
<title>Glow Haven by Marisol — Business Card</title>
<link href="https://fonts.googleapis.com/css2?family=Philosopher:wght@400;700&display=swap" rel="stylesheet">
<style>
  :root {
    --backdrop: #ecebee;
    --card-white: #ffffff;
    --magenta: #b5196f;
    --magenta-light: #d8378e;
    --magenta-deep: #8e1156;
    --leaf-green: #2f9a3a;
    --lime: #8cc63f;
    --rule-grey: #c9c9cf;
    --text-white: #ffffff;
  }
  * { box-sizing: border-box; margin: 0; padding: 0; }
  html, body { width: 1200px; height: 900px; overflow: hidden; }
  body {
    background: var(--backdrop);
    font-family: "Philosopher", sans-serif;
    position: relative;
  }
  .card {
    position: absolute;
    left: 320px;
    width: 560px;
    height: 320px;
    border-radius: 28px;
    overflow: hidden;
    background: var(--card-white);
    box-shadow: 0 6px 18px rgba(0,0,0,0.15);
  }
  .card-back { top: 100px; }
  .card-front { top: 480px; }
  .card-art { position: absolute; inset: 0; width: 100%; height: 100%; }

  /* Front */
  .brand {
    position: absolute;
    left: 110px;
    top: 40px;
    display: flex;
    align-items: center;
    gap: 18px;
  }
  .brand-dot {
    flex: none;
    width: 22px; height: 22px; border-radius: 50%;
    background: var(--magenta);
  }
  .brand-name {
    font-weight: 700;
    font-size: 38px;
    color: var(--leaf-green);
    line-height: 1.05;
  }
  .contact {
    position: absolute;
    left: 0; right: 0;
    top: 188px;
    text-align: center;
    color: var(--text-white);
  }
  .contact-name { font-weight: 700; font-size: 32px; margin-bottom: 8px; }
  .contact-line { font-weight: 700; font-size: 20px; line-height: 1.3; }

  /* Back */
  .appointment-ribbon {
    position: absolute;
    left: 0; top: 34px;
    width: 300px; height: 38px;
    background: linear-gradient(90deg, var(--magenta-deep), var(--magenta-light));
    clip-path: polygon(0 0, 100% 0, 94% 50%, 100% 100%, 0 100%);
    color: var(--text-white);
    font-size: 19px;
    font-weight: 700;
    letter-spacing: 1.5px;
    display: flex; align-items: center;
    padding-left: 28px;
  }
  .appointment-lines {
    position: absolute;
    left: 40px; right: 40px; top: 30px;
  }
  .appointment-lines span {
    display: block;
    height: 22px;
    border-bottom: 1px solid var(--rule-grey);
  }
  .appointment-lines span:nth-child(-n+2) { margin-left: 290px; }
  .website {
    position: absolute;
    right: 34px; bottom: 18px;
    color: var(--text-white);
    font-weight: 700;
    font-size: 17px;
  }
</style>
</head>
<body>

  <section class="card card-back" aria-label="Card back">
    <svg class="card-art" viewBox="0 0 560 320" preserveAspectRatio="none" aria-hidden="true">
      <path d="M0 306 C200 296 400 270 560 214 L560 320 L0 320 Z" fill="var(--leaf-green)"/>
      <path d="M0 314 C200 304 400 280 560 226 L560 320 L0 320 Z" fill="var(--magenta)"/>
    </svg>
    <div class="appointment-lines">
      <span></span><span></span><span></span><span></span>
      <span></span><span></span><span></span><span></span>
    </div>
    <div class="appointment-ribbon">Your Next Appointment</div>
    <p class="website">glowhavenbymarisol.com</p>
  </section>

  <section class="card card-front" aria-label="Card front">
    <svg class="card-art" viewBox="0 0 560 320" preserveAspectRatio="none" aria-hidden="true">
      <defs>
        <linearGradient id="frontBand" x1="0" y1="0" x2="1" y2="0">
          <stop offset="0" stop-color="#a3165f"/>
          <stop offset="0.5" stop-color="#d8378e"/>
          <stop offset="1" stop-color="#9c1462"/>
        </linearGradient>
      </defs>
      <path d="M0 142 C180 138 400 170 560 260 L560 320 L0 320 Z" fill="var(--lime)"/>
      <path d="M0 148 C180 146 400 178 560 270 L560 320 L0 320 Z" fill="var(--leaf-green)"/>
      <path d="M0 156 C180 154 400 186 560 282 L560 320 L0 320 Z" fill="url(#frontBand)"/>
    </svg>
    <div class="brand">
      <span class="brand-dot"></span>
      <span class="brand-name">Glow Haven<br>by Marisol</span>
    </div>
    <div class="contact">
      <p class="contact-name">Marisol Reyes</p>
      <p class="contact-line">148 Elm Avenue Fairview, CO 80612</p>
      <p class="contact-line">555-014-2290</p>
    </div>
  </section>

</body>
</html>
```